Web design for community centre - bright colours (provided) and matching existing logo

Website based on a provided logo and existing website template skeleton (it is a Wordpress theme we must use that is already installed)

Basically, see if you can improve the existing theme skeleton at https://tarvoshub.org.au/redesign/. Mostly we are looking for a much nicer menu that works with the logo, and a nice font/design for text content.

We have a developer who will work your design into the Wordpress theme – so you can get creative in a graphic software app and our developer can most likely implement your ideas.

The website ideally will include design ideas from the logo (e.g. the idea of people with their arms around each other, colours).

Improvement to the text displayed on the photo slider (e.g. a colour border or other decoration) is also needed.

It needs a 'community' feel.

Target Market(s)

Parents (provides childcare), older people, people with disabilities, recent migrants

Industry/Entity Type

Community Center

Number of Pages Required

1 page

Font styles to use
Sans Serif

Colors

Designer to choose colors to be used in the design.

Requirements
Must have
• A very aesthetic top menu. Nice use of spacing, negative space etc.
• Fonts need to be legally available without a pageview fee (one off purchase OK). You need to provide proof we can use the font legally.
• See https://www.plover.org.au/ for an example of a menu we like.
• Must use the existing logo, provided in this brief.
• Needs to use colours from the logo but do not need to use all of them!
• Must be workable into the theme already installed at https://tarvoshub.org.au/redesign
Nice to have
• Maybe some kind of shapes attached to each menu link (top menu0
• A use of all 5 colours on the top menu, when you hover on it
Should not have
• Serif fonts

```html
<!DOCTYPE html>
<html lang="en">
<head>
<meta charset="utf-8">
<title>Tarvos Neighbourhood Learning Centre</title>
<link href="https://fonts.googleapis.com/css2?family=Exo+2:ital,wght@0,300;0,400;0,500;0,600;0,700;1,400&display=swap" rel="stylesheet">
<style>
:root{
  --pink:#e8196b;--purple:#6a2c91;--green:#8dc63f;--orange:#f7941d;--blue:#1ba6e0;
  --yellow:#fdd023;--navy:#1a2f8a;--ink:#1b1b1b;--text:#333;--grey-bg:#f7f7f7;--white:#fff;
}
*{box-sizing:border-box;margin:0;padding:0}
html,body{width:1200px;height:2250px;overflow:hidden}
body{position:relative;background:var(--white);font-family:'Exo 2',sans-serif;color:var(--text)}
.abs{position:absolute}
.rainbow{position:absolute;left:0;width:1200px;height:3px;display:flex}
.rainbow span{flex:1}
.rainbow span:nth-child(1){background:var(--pink)}
.rainbow span:nth-child(2){background:var(--purple)}
.rainbow span:nth-child(3){background:var(--green)}
.rainbow span:nth-child(4){background:var(--orange)}
.rainbow span:nth-child(5){background:var(--blue)}

/* header */
.brand{left:234px;top:24px;display:flex;align-items:center;gap:10px}
.brand-dot{width:52px;height:52px;border-radius:50%;border:6px solid var(--blue)}
.brand-name{font-size:16px;font-weight:600;line-height:17px;color:var(--ink)}
.phone{left:788px;top:48px;font-size:11px;font-weight:600;color:var(--ink);display:flex;align-items:center;gap:6px}
.donate{left:887px;top:38px;width:78px;height:31px;border-radius:16px;background:var(--yellow);font-size:10px;font-weight:700;color:var(--ink);display:flex;align-items:center;justify-content:center}
.nav{left:234px;top:103px;display:flex}
.nav a{font-size:10px;font-weight:600;color:var(--blue);text-decoration:none;text-transform:uppercase;padding-top:17px;position:relative;margin-right:34px}
.nav a::before{content:"";position:absolute;left:0;top:0;height:3px;width:calc(100% - 2px);background:#e9e9e9}
.nav a.current{color:var(--pink)}
.nav a.current::before{width:26px}
.search{left:939px;top:111px;width:25px;height:25px;border-radius:50%;background:var(--blue);display:flex;align-items:center;justify-content:center}

/* hero */
.grey-zone{left:0;top:152px;width:1200px;height:949px;background:var(--grey-bg)}
.hero{left:59px;top:152px;width:1081px;height:446px;background:linear-gradient(90deg,#4a2e1f,#7a5236 35%,#5e3d28 60%,#8a6244)}
.hero-caption{left:403px;top:309px;width:393px;height:158px;background:rgba(40,28,22,.78);border-top:2px solid var(--orange);padding:24px 28px 0 25px;color:var(--white)}
.hero-caption h2{font-size:15px;font-weight:600;padding-bottom:7px;border-bottom:1px solid rgba(255,255,255,.7)}
.hero-caption p{font-size:14px;font-weight:300;line-height:21px;margin-top:12px}
.hero-arrow{top:361px;width:32px;height:32px;background:#111;display:flex;align-items:center;justify-content:center}

/* welcome */
.welcome{left:234px;top:657px;width:554px;height:374px;background:var(--white)}
.welcome h1{position:absolute;left:27px;top:46px;font-size:20px;font-weight:700;color:var(--ink)}
.welcome-copy{position:absolute;left:26px;top:80px;width:331px;font-size:11.5px;line-height:18.8px;text-align:justify;color:#333}
.welcome-copy p+p{margin-top:18px}
.btn{position:absolute;top:295px;height:32px;color:var(--white);font-size:11px;font-weight:600;display:flex;align-items:center;justify-content:center;text-transform:uppercase}
.btn-orange{left:24px;width:145px;background:var(--orange)}
.btn-blue{left:180px;width:86px;background:var(--blue)}
.video{left:609px;top:700px;width:357px;height:289px;background:linear-gradient(135deg,#a6b84a,#8ea83a 50%,#b2c25a)}
.play{left:766px;top:827px;width:40px;height:40px;border-radius:50%;background:#ec3c4c;display:flex;align-items:center;justify-content:center}

/* courses */
.section-title{font-size:25px;font-weight:700;color:var(--ink);text-transform:uppercase}
.center-title{left:0;width:1200px;top:1161px;text-align:center}
.rule{height:2px;width:43px;background:var(--navy)}
.courses{left:0;top:1233px;width:1200px;height:359px;background:linear-gradient(90deg,#2bb0dc,#1d9fd6 50%,#128bc9)}
.course-highlight{left:337px;top:1233px;width:175px;height:359px;background:rgba(88,80,180,.78)}
.divider{top:1283px;width:1px;height:309px;background:rgba(255,255,255,.25)}
.course{width:175px;text-align:center;color:var(--white)}
.course h3{font-size:19px;font-weight:600;line-height:22px;text-transform:uppercase}
.course .date{font-size:8.5px;margin-top:9px}
.course .more{font-size:8.5px;margin-top:22px;display:inline-block;position:relative;padding:0 0 3px}
.course .more::before,.course .more::after{content:"";position:absolute;left:50%;width:18px;margin-left:-9px;height:1px;background:var(--white)}
.course .more::before{top:-6px}
.course .more::after{bottom:-3px}
.slider-btn{top:1402px;width:38px;height:38px;border-radius:50%;background:rgba(10,40,90,.45);display:flex;align-items:center;justify-content:center}

/* testimonial */
.quote-card{left:234px;top:1724px;width:357px;height:160px;border:1px solid #ddd;border-radius:4px;padding:22px 21px}
.stars{color:#e8303a;font-size:10px;letter-spacing:2px}
.quote-card h4{font-size:9.5px;font-weight:600;color:var(--ink);line-height:13px;margin-top:8px;text-transform:uppercase}
.quote-card p{font-size:8.2px;line-height:14px;margin-top:9px;color:#444}
.avatar{left:522px;top:1861px;width:56px;height:56px;border-radius:50%;background:linear-gradient(160deg,#4a4a4a,#222)}
.quote-mark{left:559px;top:1890px;width:28px;height:28px;border-radius:50%;background:var(--purple);color:var(--white);font-size:16px;font-weight:700;display:flex;align-items:center;justify-content:center}
.author{left:428px;top:1902px;font-size:10.5px;font-weight:600;color:var(--ink)}

/* events */
.event{left:609px;width:357px;background:#efefef;display:flex;align-items:center;font-size:8.5px;color:var(--ink)}
.event .tag{width:45px;height:100%;color:var(--white);font-weight:700;display:flex;align-items:center;justify-content:center;font-size:8px}
.event .name{margin-left:12px;font-weight:600;text-transform:uppercase}
.event .when{font-style:italic;color:#555;margin-left:4px;text-transform:uppercase}
.event .toggle{margin-left:auto;margin-right:13px;width:13px;height:13px;border-radius:50%;background:var(--ink);color:var(--white);font-size:11px;line-height:13px;text-align:center}
.event .toggle.open{background:var(--white);color:var(--ink);border:1px solid #ccc;line-height:10px}
.event-body{left:609px;top:1830px;width:357px;height:61px;border:1px solid #ddd;border-top:none;padding:18px 12px;font-size:8.5px;line-height:13px;color:#333}
.read-all{left:609px;top:1910px;font-size:8.5px;font-style:italic;color:var(--navy)}

/* footer */
.footer{left:0;top:1981px;width:1200px;height:269px;background:var(--yellow)}
.badge{top:2021px;height:46px}
.contact{top:2108px;display:flex;gap:10px;font-size:12.5px;line-height:18px;color:var(--ink)}
.social{top:2114px;width:21px;height:21px;border-radius:50%;border:1.5px solid var(--ink)}
.footer-rule{left:235px;top:2175px;width:732px;height:1px;background:rgba(0,0,0,.2)}
.copyright{left:0;width:1200px;top:2208px;text-align:center;font-size:8.5px;color:var(--ink)}
</style>
</head>
<body>
<div class="rainbow" style="top:0"><span></span><span></span><span></span><span></span><span></span></div>

<header>
  <div class="abs brand"><div class="brand-dot"></div><div class="brand-name">Tarvos<br>Neighbourhood<br>Learning Centre</div></div>
  <div class="abs phone">
    <svg width="12" height="12" viewBox="0 0 24 24"><path fill="#f7b500" d="M6.6 10.8a15 15 0 0 0 6.6 6.6l2.2-2.2c.3-.3.7-.4 1-.2 1.1.4 2.3.6 3.6.6.6 0 1 .4 1 1V20c0 .6-.4 1-1 1A17 17 0 0 1 3 4c0-.6.4-1 1-1h3.5c.6 0 1 .4 1 1 0 1.3.2 2.5.6 3.6.1.3 0 .7-.2 1z"/></svg>
    03 9000 4127
  </div>
  <div class="abs donate">DONATE</div>
  <nav class="abs nav">
    <a class="current" href="#">Home</a><a href="#">Courses</a><a href="#">Social Enterprise</a><a href="#">Community Programs</a><a href="#">Tarvos Cares</a><a href="#">Venue Hire</a><a href="#">Spareseat Café</a>
  </nav>
  <div class="abs search"><svg width="10" height="10" viewBox="0 0 10 10"><circle cx="4.2" cy="4.2" r="2.8" fill="none" stroke="#fff" stroke-width="1.3"/><line x1="6.3" y1="6.3" x2="8.6" y2="8.6" stroke="#fff" stroke-width="1.3"/></svg></div>
</header>

<div class="abs grey-zone"></div>
<div class="abs hero" role="img" aria-label="Photo of several hands of different people resting together on a wooden table"></div>
<div class="abs hero-caption">
  <h2>HANDS</h2>
  <p>Our accredited Childcare and Kinder allows your child to grown in a fun learning environment, while you attend courses or activities</p>
</div>
<div class="abs hero-arrow" style="left:59px"><svg width="10" height="14" viewBox="0 0 10 14"><path d="M8 1 2 7l6 6" fill="none" stroke="#f7941d" stroke-width="2"/></svg></div>
<div class="abs hero-arrow" style="left:1108px"><svg width="10" height="14" viewBox="0 0 10 14"><path d="m2 1 6 6-6 6" fill="none" stroke="#f7941d" stroke-width="2"/></svg></div>

<section class="abs welcome">
  <h1>WELCOME TO TNLC</h1>
  <div class="welcome-copy">
    <p>Civic Spark Consulting supports nonprofit organizations and educational institutions to carry out their missions to benefit the wider community.</p>
    <p>Founder Mara Velen is an educator with a 22-year record of demonstrated achievement and leadership roles in nonprofits and educational institutions. Most recently, she served as Associate Dean of Students in the University and Director of the University Community Service Center at the University of Eastvale. Mara has designed, implemented</p>
  </div>
  <div class="btn btn-orange">View Course Brochure</div>
  <div class="btn btn-blue">Enrol Now</div>
</section>
<div class="abs video" role="img" aria-label="Video still of a community choir group singing in a classroom"></div>
<div class="abs play"><svg width="12" height="14" viewBox="0 0 12 14"><path d="M1 0v14l11-7z" fill="#fff"/></svg></div>

<h2 class="abs section-title center-title">Courses Starting Soon</h2>
<div class="abs rule" style="left:579px;top:1198px"></div>

<div class="abs courses" role="img" aria-label="Blue-tinted photo of a group of people at a community class"></div>
<div class="abs course-highlight"></div>
<div class="abs divider" style="left:512px"></div>
<div class="abs divider" style="left:687px"></div>
<div class="abs divider" style="left:863px"></div>

<div class="abs course" style="left:167px;top:1338px"><h3>Barista<br>Training</h3><div class="date">Monday 16th September</div><span class="more">READ MORE</span></div>
<div class="abs course" style="left:336px;top:1338px"><h3>Be<br>Connected</h3><div class="date">Wednesday 18th September</div><span class="more">READ MORE</span></div>
<div class="abs course" style="left:512px;top:1327px"><h3>Lisa’s Class<br>for the Young<br>at Heart</h3><div class="date" style="margin-top:1px">Monday 7th October</div><span class="more" style="margin-top:18px">READ MORE</span></div>
<div class="abs course" style="left:687px;top:1345px"><h3>Ukulele</h3><div class="date">Monday 7th October</div><span class="more" style="margin-top:40px">READ MORE</span></div>
<div class="abs course" style="left:863px;top:1323px"><h3>Tai Chi<br>Arthritis</h3><div class="date">Monday 7th October</div><span class="more" style="margin-top:40px">READ MORE</span></div>

<div class="abs slider-btn" style="left:125px"><svg width="10" height="16" viewBox="0 0 10 16"><path d="M8 1 2 8l6 7" fill="none" stroke="#fff" stroke-width="2"/></svg></div>
<div class="abs slider-btn" style="left:1037px"><svg width="10" height="16" viewBox="0 0 10 16"><path d="m2 1 6 7-6 7" fill="none" stroke="#fff" stroke-width="2"/></svg></div>

<h2 class="abs section-title" style="left:234px;top:1657px">Testimonial</h2>
<div class="abs rule" style="left:234px;top:1694px"></div>
<div class="abs quote-card">
  <div class="stars">★★★★★</div>
  <h4>Lorem ipsum dolor sit amet, consectetur adipiscing elit.<br>Donec ligula ipsum, accumsan nec nulla eget</h4>
  <p>Morbi condimentum, leo sed efficitur euismod, ante risus gravida lacus, ut congue erat arcu vel dui. Phasellus ultricies consequat ipsum, nec lobortis odio scelerisque et.</p>
</div>
<div class="abs author">DL &nbsp;|&nbsp; STUDENT</div>
<div class="abs avatar" role="img" aria-label="Portrait photo of the student"></div>
<div class="abs quote-mark">“</div>

<h2 class="abs section-title" style="left:609px;top:1657px">What's On</h2>
<div class="abs rule" style="left:609px;top:1694px"></div>

<div class="abs event" style="top:1721px;height:27px"><span class="tag" style="background:var(--blue)">11 SEP</span><span class="name">Merrin River Cruise Excursion</span><span class="when">&nbsp;- Wednesday 11th September</span><span class="toggle">+</span></div>
<div class="abs event" style="top:1760px;height:27px"><span class="tag" style="background:var(--navy)">11 SEP</span><span class="name">Tarvos Cares</span><span class="toggle">+</span></div>
<div class="abs event" style="top:1799px;height:31px"><span class="tag" style="background:var(--pink)">11 SEP</span><span class="name">TNLC Short Films</span><span class="toggle open">-</span></div>
<div class="abs event-body">Check out our new Vidlo and Streamly channels! Now you can view all the amazing work that goes on at TNLC</div>
<div class="abs read-all">Read All News &nbsp;→</div>

<footer>
  <div class="abs footer"></div>
  <div class="rainbow" style="top:1979px"><span></span><span></span><span></span><span></span><span></span></div>
  <div class="abs badge" style="left:473px;width:79px;background:#1c3a8f"></div>
  <div class="abs badge" style="left:570px;width:82px;background:#fff"></div>
  <div class="abs badge" style="left:670px;width:59px;background:#fff"></div>

  <div class="abs contact" style="left:236px">
    <svg width="15" height="20" viewBox="0 0 15 20"><path d="M7.5 1A6 6 0 0 0 1.5 7c0 4.5 6 12 6 12s6-7.5 6-12a6 6 0 0 0-6-6z" fill="none" stroke="#e8196b" stroke-width="1.4"/><circle cx="7.5" cy="7" r="2.2" fill="none" stroke="#e8196b" stroke-width="1.4"/></svg>
    <div>14 Larkin St,<br>Tarvos, VIC, 3999</div>
  </div>
  <div class="abs contact" style="left:436px">
    <svg width="20" height="20" viewBox="0 0 24 24"><path d="M6.6 10.8a15 15 0 0 0 6.6 6.6l2.2-2.2c.3-.3.7-.4 1-.2 1.1.4 2.3.6 3.6.6.6 0 1 .4 1 1V20c0 .6-.4 1-1 1A17 17 0 0 1 3 4c0-.6.4-1 1-1h3.5c.6 0 1 .4 1 1 0 1.3.2 2.5.6 3.6.1.3 0 .7-.2 1z" fill="none" stroke="#e8196b" stroke-width="1.4"/></svg>
    <div>Call Us<br>03 9000 4127</div>
  </div>
  <div class="abs contact" style="left:632px">
    <svg width="21" height="16" viewBox="0 0 21 16" style="margin-top:3px"><rect x="0.5" y="0.5" width="20" height="15" rx="1.5" fill="#e8196b"/><path d="M1 1.5 10.5 9 20 1.5" fill="none" stroke="#fdd023" stroke-width="1.3"/></svg>
    <div>Email Us<br>admin@tarvoshub.org.au</div>
  </div>
  <div class="abs social" style="left:860px"></div>
  <div class="abs social" style="left:886px"></div>
  <div class="abs social" style="left:912px"></div>
  <div class="abs social" style="left:938px"></div>

  <div class="abs footer-rule"></div>
  <div class="abs copyright">© 2019 Tarvos Neighbourhood Learning Centre. All Rights Reserved. Policies &amp; Procedures.</div>
</footer>
</body>
</html>
```